The Brightwater Compass Business Card

We need an attractive business card with the logo that we bought from ArtVantly last year.
Our mission is to contribute to change the way today's leaders manage business companies bringing value to the workplace and helping them to build a new model of creating wealth.
Our logo is clear about our values : we seek Positive Change through People and are convinced that the pursuit of individual well-being and the chase of economic results can converge with the right management.
Management Consulting
Corinne Fabrelle
+34 612 98 70 31
corinne.fabrelle@thebrightwatercompass-mail.net
www.thebrightwatercompass-mail.net

```html
<!DOCTYPE html>
<html lang="en">
<head>
<meta charset="utf-8">
<title>The Brightwater Compass — Business Card</title>
<link rel="stylesheet" href="https://fonts.googleapis.com/css2?family=Roboto:ital,wght@0,400;0,700;1,400;1,700&display=swap">
<style>
  :root {
    --backdrop: #6b7276;
    --teal: #03807e;
    --teal-light: #82cfc6;
    --paper: #ffffff;
    --ink-light: #ffffff;
  }
  * { box-sizing: border-box; margin: 0; padding: 0; }
  html, body { width: 1200px; height: 900px; overflow: hidden; }
  body {
    background: var(--backdrop);
    display: flex;
    flex-direction: column;
    align-items: center;
    justify-content: center;
    gap: 56px;
    font-family: "Roboto", sans-serif;
  }
  .card {
    position: relative;
    width: 640px;
    height: 366px;
    border-radius: 22px;
    overflow: hidden;
    background: var(--teal);
  }

  /* Brand name: one colour, one weight, one plain circle beside it */
  .brand {
    display: flex;
    align-items: center;
    justify-content: center;
    gap: 12px;
    font-weight: 400;
    line-height: 1.2;
  }
  .brand-dot { flex: none; border-radius: 50%; background: currentColor; }

  /* Back of card */
  .card-back {
    display: flex;
    flex-direction: column;
    align-items: center;
    justify-content: center;
    color: var(--ink-light);
  }
  .card-back .brand-name { font-size: 36px; }
  .card-back .brand-dot { width: 16px; height: 16px; }
  .card-back .website {
    margin-top: 40px;
    font-size: 17px;
    letter-spacing: 0.3px;
  }

  /* Front of card */
  .card-front .shape { position: absolute; inset: 0; }
  .contact-side {
    position: absolute;
    left: 36px;
    top: 48px;
    color: var(--ink-light);
  }
  .person-name { font-size: 21px; font-weight: 700; font-style: italic; }
  .person-role { font-size: 12px; font-style: italic; letter-spacing: 1px; margin-top: 2px; }
  .contact-list { list-style: none; margin-top: 40px; }
  .contact-list li {
    display: flex; align-items: center; gap: 8px;
    font-size: 10.5px; font-style: italic; margin-bottom: 9px;
    white-space: nowrap;
  }
  .contact-list svg { width: 11px; height: 11px; flex: none; }
  .brand-front {
    position: absolute;
    left: 400px;
    right: 24px;
    top: 150px;
    color: var(--teal);
  }
  .brand-front .brand-name { font-size: 22px; text-align: center; }
  .brand-front .brand-dot { width: 12px; height: 12px; }
</style>
</head>
<body>

  <section class="card card-front" aria-label="Business card front">
    <svg class="shape" viewBox="0 0 640 366" aria-hidden="true">
      <circle cx="716" cy="200" r="348" fill="var(--teal-light)"/>
      <circle cx="722" cy="200" r="340" fill="var(--teal)"/>
      <circle cx="728" cy="200" r="334" fill="var(--paper)"/>
    </svg>

    <div class="contact-side">
      <p class="person-name">Corinne Fabrelle</p>
      <p class="person-role">FOUNDER</p>
      <ul class="contact-list">
        <li>
          <svg viewBox="0 0 24 24" aria-hidden="true"><path fill="#fff" d="M6.6 10.8a15 15 0 0 0 6.6 6.6l2.2-2.2a1 1 0 0 1 1-.25 11.4 11.4 0 0 0 3.6.57 1 1 0 0 1 1 1V20a1 1 0 0 1-1 1A17 17 0 0 1 3 4a1 1 0 0 1 1-1h3.5a1 1 0 0 1 1 1c0 1.25.2 2.45.57 3.57a1 1 0 0 1-.25 1z"/></svg>
          +34 612 98 70 31
        </li>
        <li>
          <svg viewBox="0 0 24 24" aria-hidden="true"><rect x="2" y="5" width="20" height="14" rx="1" fill="none" stroke="#fff" stroke-width="2"/><path d="M2 6l10 7 10-7" fill="none" stroke="#fff" stroke-width="2"/></svg>
          corinne.fabrelle@thebrightwatercompass-mail.net
        </li>
        <li>
          <svg viewBox="0 0 24 24" aria-hidden="true"><circle cx="12" cy="12" r="10" fill="none" stroke="#fff" stroke-width="2"/><path d="M2 12h20M12 2c3 3 3 17 0 20M12 2c-3 3-3 17 0 20" fill="none" stroke="#fff" stroke-width="1.6"/></svg>
          www.thebrightwatercompass-mail.net
        </li>
      </ul>
    </div>

    <div class="brand brand-front">
      <span class="brand-dot"></span>
      <p class="brand-name">The Brightwater Compass</p>
    </div>
  </section>

  <section class="card card-back" aria-label="Business card back">
    <div class="brand">
      <span class="brand-dot"></span>
      <p class="brand-name">The Brightwater Compass</p>
    </div>
    <p class="website">www.thebrightwatercompass-mail.net</p>
  </section>

</body>
</html>
```